Halvo KT Biz Card Design

Residential / Commercial/ Emergency

Industry/Entity Type

Residential

Contact Information for Business Card

Tomas Welker
President
PO Box 4827
East Quogue, NY 11942
tomas@halvo-kt.com
631.555.0172
855.HALVO.KT
www.halvo-kt.com
FB: Halvo KT
Twitter: HALVO KT

```html
<!DOCTYPE html>
<html lang="en">
<head>
<meta charset="utf-8">
<title>Halvo KT Business Card</title>
<link href="https://fonts.googleapis.com/css2?family=Oswald:wght@500;700&display=swap" rel="stylesheet">
<style>
  :root {
    --bg: #e9e6e1;
    --card-white: #f7f7f5;
    --charcoal: #2b3035;
    --orange: #eea321;
    --ink: #2a2d31;
    --white: #ffffff;
    --social: #3f72a8;
  }
  * { margin: 0; padding: 0; box-sizing: border-box; }
  html, body { width: 1200px; height: 885px; overflow: hidden; }
  body {
    background: var(--bg);
    font-family: "Oswald", "Arial Narrow", sans-serif;
    position: relative;
  }
  .card {
    position: absolute;
    left: 320px;
    width: 560px;
    height: 320px;
    background: var(--card-white);
    overflow: hidden;
    box-shadow: 0 6px 18px rgba(0,0,0,.18);
  }
  .card--front { top: 80px; }
  .card--back { top: 485px; }

  /* Front */
  .front-header {
    position: absolute; left: 0; top: 0; width: 100%; height: 112px;
    display: flex; align-items: center; justify-content: space-between;
    padding: 0 26px;
  }
  .brand-name {
    color: var(--orange); font-weight: 700; font-size: 74px;
    line-height: 1; letter-spacing: -1px;
  }
  .person { text-align: right; line-height: 1.05; }
  .person-name { color: var(--ink); font-weight: 700; font-size: 30px; }
  .person-title { color: var(--orange); font-weight: 700; font-size: 22px; }

  .photo-row {
    position: absolute; left: 0; top: 112px; width: 100%; height: 118px;
    display: flex;
  }
  .photo { flex: 1; }
  .photo--landscape { background: linear-gradient(180deg, #8fbbe2 0%, #b8d4e6 30%, #7fae3e 45%, #5e8f2a 100%); }
  .photo--survey { background: linear-gradient(160deg, #f2f2ef 0%, #d9ddd5 55%, #a9b992 100%); }
  .photo--field { background: linear-gradient(135deg, #6f8c4a 0%, #c23a2c 55%, #d94a3a 100%); }

  .front-footer {
    position: absolute; left: 0; bottom: 0; width: 100%; height: 90px;
    background: var(--charcoal);
    display: flex; align-items: center; justify-content: space-between;
    padding: 0 24px;
  }
  .web-large { color: var(--white); font-weight: 700; font-size: 36px; }
  .contact-list { list-style: none; color: var(--white); font-weight: 500; font-size: 17px; }
  .contact-list li { display: flex; align-items: center; gap: 8px; line-height: 1.45; }
  .contact-icon { width: 18px; height: 18px; display: block; }

  /* Back */
  .back-top {
    position: absolute; left: 0; top: 0; width: 100%; height: 58px;
    background: var(--charcoal);
    display: flex; align-items: center; justify-content: center;
  }
  .web-small { color: var(--white); font-weight: 700; font-size: 22px; letter-spacing: 2px; }
  .back-middle {
    position: absolute; left: 0; top: 58px; width: 100%; height: 170px;
    display: flex; align-items: center; justify-content: center;
  }
  .brand-name--large { font-size: 118px; }
  .social-links {
    position: absolute; right: 14px; bottom: 14px;
    display: flex; flex-direction: column; gap: 6px;
  }
  .social-square { width: 26px; height: 26px; background: var(--social); border-radius: 3px; }
  .back-bottom {
    position: absolute; left: 0; bottom: 0; width: 100%; height: 92px;
    background: var(--charcoal);
    display: flex; flex-direction: column; justify-content: center;
    padding: 0 24px; color: var(--white); font-weight: 700; font-size: 16px; line-height: 1.5;
  }
</style>
</head>
<body>

<section class="card card--front">
  <header class="front-header">
    <div class="brand-name">HALVO-KT</div>
    <div class="person">
      <div class="person-name">Tomas Welker</div>
      <div class="person-title">President</div>
    </div>
  </header>

  <div class="photo-row">
    <div class="photo photo--landscape" role="img" aria-label="Aerial photo of green countryside with a house"></div>
    <div class="photo photo--survey" role="img" aria-label="Drone mapping illustration over terrain"></div>
    <div class="photo photo--field" role="img" aria-label="Search team member operating a drone outdoors"></div>
  </div>

  <footer class="front-footer">
    <div class="web-large">www.halvo-kt.com</div>
    <ul class="contact-list">
      <li>
        <svg class="contact-icon" viewBox="0 0 18 18" aria-hidden="true">
          <rect width="18" height="18" rx="2" fill="#eea321"/>
          <path d="M5 4.5c.8-.5 1.4-.2 1.8.5l.7 1.3c.3.6.1 1.1-.4 1.4l-.5.3c.6 1.3 1.5 2.2 2.8 2.8l.3-.5c.3-.5.8-.7 1.4-.4l1.3.7c.7.4 1 1 .5 1.8-.6 1-1.8 1.3-3 .8C7.3 12 6 10.7 5 8.1c-.5-1.3-.9-2.8 0-3.6z" fill="#fff"/>
        </svg>
        631.555.0172
      </li>
      <li>
        <svg class="contact-icon" viewBox="0 0 18 18" aria-hidden="true">
          <rect width="18" height="18" rx="2" fill="#eea321"/>
          <rect x="3.5" y="5" width="11" height="8" fill="none" stroke="#fff" stroke-width="1.4"/>
          <path d="M3.5 5l5.5 4.5L14.5 5" fill="none" stroke="#fff" stroke-width="1.4"/>
        </svg>
        tomas@halvo-kt.com
      </li>
    </ul>
  </footer>
</section>

<section class="card card--back">
  <div class="back-top">
    <div class="web-small">www.halvo-kt.com</div>
  </div>
  <div class="back-middle">
    <div class="brand-name brand-name--large">HALVO-KT</div>
  </div>
  <div class="social-links" aria-label="Social links">
    <span class="social-square"></span>
    <span class="social-square"></span>
  </div>
  <footer class="back-bottom">
    <p>Cellular Towers-Comm/Ind Security-Construction-Inspections</p>
    <p>Disaster Views-Public Safety-Search &amp; Rescue-Surveys</p>
  </footer>
</section>

</body>
</html>
```